The Quiet Pantry Method: Reshape Your Habits Around Meals in Only 30 Days

I want a book cover for a paperback non-fiction book 30 day challenge to transform you relationship with your food, diet and lifestyle for longterm health and vitality. I would like to incorporate two photos on the front cover, one of a Greek salad and one of me the author. I have uploaded the four photos. Use which of each pair you think best. Because of my name, I want the photo on the cover. Otherwise folks assume Marla is a guy.
I am looking at best selling health books and they seem to be on the lighter side color-wise, with horizontal design. Green and orange seem to work most often, though my logo is a bluish turquoise (https://marlavoskin.com). I would imagine a light background, clear simple fonts. Looking forward to your designs!

Target Market(s)

Women around 35-40 confused by conflicting nutrition information but dedicated to better health haelthy

Industry/Entity Type

nutrition and wellness

Font styles to use
Serif

Colors
00AB8E
00BBA5
67D7C9
C6EFE9
E9F9F6
F0912C
F2A743
F7CA91
FBE8D2
FDF5EE
EE7325
F08F49
F5BC92
FAE3D3
FDF4ED

Requirements
Must have
• Clear simple look with room for an endorsement
Nice to have
• Hints of natural scenes and happy places
Should not have
• Dark or ominous feel

```html
<!DOCTYPE html>
<html lang="en">
<head>
<meta charset="utf-8">
<title>The Quiet Pantry Method – Marla Voskin</title>
<link rel="stylesheet" href="https://fonts.googleapis.com/css2?family=Jost:wght@300;400&display=swap">
<style>
  :root {
    --teal: #5ab0b4;
    --teal-band: #5db1b5;
    --white: #ffffff;
    --paper: #ffffff;
  }
  html, body { margin: 0; padding: 0; overflow: hidden; background: var(--paper); }
  .cover {
    position: relative;
    width: 930px;
    height: 1200px;
    overflow: hidden;
    background: var(--paper);
    font-family: "Jost", sans-serif;
    font-weight: 300;
  }
  .author-band {
    position: absolute; left: 0; top: 94px;
    width: 100%; height: 162px;
    background: var(--teal-band);
  }
  .author-name {
    position: absolute; right: 294px; top: 126px;
    margin: 0;
    font-size: 74px; font-weight: 300;
    color: var(--white);
    line-height: 1;
    text-align: right;
    white-space: nowrap;
  }
  .author-portrait {
    position: absolute; left: 654px; top: 110px;
    width: 196px; height: 196px;
    border-radius: 50%;
    border: 4px solid var(--white);
    background: radial-gradient(circle at 50% 55%, #d9a99a 0%, #8a5a4c 38%, #2b1d1a 70%);
  }
  .title {
    position: absolute; left: 0; top: 328px;
    width: 100%;
    margin: 0;
    text-align: center;
    color: var(--teal);
    font-weight: 300;
    font-size: 100px;
    line-height: 134px;
    letter-spacing: -1px;
    text-transform: uppercase;
    white-space: nowrap;
  }
  .title span { display: block; }
  .salad-photo {
    position: absolute; left: 164px; top: 628px;
    width: 628px; height: 262px;
    border-radius: 50%;
    background: radial-gradient(ellipse at 50% 45%, #d8412b 0%, #c93a27 30%, #6d8f3b 55%, #b8c3c9 75%, #dfe4e6 100%);
  }
  .subtitle {
    position: absolute; left: 0; top: 946px;
    width: 100%;
    margin: 0;
    text-align: center;
    color: var(--teal);
    font-size: 38px; font-weight: 300;
    line-height: 1;
    white-space: nowrap;
  }
  .timeframe-band {
    position: absolute; left: 0; top: 996px;
    width: 100%; height: 100px;
    background: var(--teal-band);
  }
  .timeframe {
    position: absolute; left: 0; top: 1010px;
    width: 100%;
    margin: 0;
    text-align: center;
    color: var(--white);
    font-size: 58px; font-weight: 300;
    line-height: 1.2;
    white-space: nowrap;
  }
</style>
</head>
<body>
  <main class="cover">
    <div class="author-band"></div>
    <p class="author-name">Marla Voskin</p>
    <div class="author-portrait" role="img" aria-label="Circular portrait photo of the author"></div>

    <h1 class="title"><span>The Quiet</span><span>Pantry Method:</span></h1>

    <div class="salad-photo" role="img" aria-label="Photo of a Greek salad with feta, olives, tomatoes and cucumber on a plate"></div>

    <p class="subtitle">Reshape Your Habits Around Meals</p>
    <div class="timeframe-band"></div>
    <p class="timeframe">in Only 30 Days</p>
  </main>
</body>
</html>
```